Lumora Learning Web Design Project

Who We are:
Lumora Learning is education information portal/ magazine, providing information about the Chinese and International education markets. Our aim is to help school principals improve there curriculum, and parents in understanding this curriculum.

Project Brief:
The site will include education news updates, educational services, curriculum developments and overseas study. We hope the site represents the cross cultural bridge between the west and east. The site will cover both the Sciences and Arts.

Note:
The logo design competition is also underway so we only need the website design

What We want:
This competition is for Design only no coding!
Design a home page based on Template 1,2 or 3. I only need to select one.
The design of an article page.

Optional
Design a Microsoft Windows metro style splash page.

Sites We like:
http://www.kavelin.com.cn/kavelinlingo/default.aspx
http://www.brixtalacademia.co.uk/
http://qrpv.norvatestudio.net/

Template Explanations:
Template 1-
The main information has a dynamic sliding category view that when clicked displays the relevant info.
In addition to the main upper menu it also has a left hand sliding menu that pops out on click or gesture

Template 2-
Has limited number of Articles most of the menus are drop downs from the top menu

Template 3-
No Top menu

Target Market(s)

Teachers, principals and parents

Industry/Entity Type

Education

Requirements
Should not have
• kindergarten preschool feel

```html
<!DOCTYPE html>
<html lang="en">
<head>
<meta charset="utf-8">
<title>Lumora Learning</title>
<link href="https://fonts.googleapis.com/css2?family=Arimo:wght@400;700&family=Roboto+Condensed:wght@400;700&family=Open+Sans:wght@400;600&display=swap" rel="stylesheet">
<style>
:root{
  --page:#e6e6e6;--white:#fff;--ink:#222;--link:#1a4e86;--muted:#555;
  --green:#4b9a3a;--blue:#1f63a9;--orange:#f6b019;
  --nav-top:#3a3a3a;--nav-bot:#111;--accent:#f2a51b;
  --ad:#0f4b86;--ad-band:#0a3763;--ad-hi:#ffffff;
  --foot:#3f3f3f;--foot-text:#ddd;--panel:#f7f7f7;--line:#dcdcdc;
}
*{box-sizing:border-box;margin:0;padding:0}
html,body{width:1200px;height:1151px;overflow:hidden}
body{background:var(--page);font-family:Arimo,Arial,sans-serif;color:var(--ink);position:relative}
.page{position:absolute;left:102px;top:0;width:996px;height:942px;background:var(--white)}
.abs{position:absolute}
.brand{left:24px;top:40px;display:flex;align-items:center;gap:10px;font-family:"Open Sans",sans-serif;font-size:32px;color:#333}
.brand i{width:26px;height:26px;border-radius:50%;background:var(--green);display:block}
.search{left:737px;top:44px;width:221px;height:38px;border:2px solid #ccc;border-radius:20px;background:#f3f3f3;color:#999;font-size:15px;padding:8px 12px}
.search svg{position:absolute;right:12px;top:8px}
.nav{left:0;top:115px;width:996px;height:46px;background:linear-gradient(var(--nav-top),var(--nav-bot));display:flex;font-family:"Open Sans",sans-serif;font-size:14px;font-weight:600;color:#fff}
.nav a{padding:0 22px;line-height:44px;border-right:1px solid #000;box-shadow:1px 0 0 #444}
.nav a.on{border-bottom:3px solid var(--accent)}
.tag{left:11px;width:72px;height:25px;font-family:"Roboto Condensed",sans-serif;font-weight:700;font-size:14px;color:#fff;line-height:25px;padding-left:6px;clip-path:polygon(0 0,85% 0,100% 50%,85% 100%,0 100%)}
.g{background:var(--green)}.b{background:var(--blue)}.o{background:var(--orange)}
.follow{left:14px;top:585px;width:70px;height:327px;background:#ddd;border:3px solid #eee;text-align:center;font-family:"Roboto Condensed",sans-serif;font-size:22px;line-height:26px}
.follow .rail{position:absolute;left:32px;top:90px;width:3px;height:200px;background:#fff}
.soc{position:relative;width:52px;height:52px;border-radius:50%;background:#fff;border:3px solid #ccc;margin:12px auto 0;font-family:Arimo,sans-serif;font-size:8.5px;color:#777;line-height:46px;overflow:hidden}
.photo{background:linear-gradient(135deg,#6d6561,#b59d8f 50%,#4a3e3a)}
.cat{left:95px;top:480px;width:579px;height:432px;background:var(--panel);border:1px solid var(--line)}
.cat h2{height:45px;background:linear-gradient(#3b3b3b,#050505);color:#fff;font-family:"Roboto Condensed",sans-serif;font-weight:400;font-size:26px;letter-spacing:1px;padding:6px 16px}
.col{position:absolute;top:63px;width:262px}
.col .pic{width:236px;height:133px;border:3px solid #ddd}
.col h3{font-size:14px;color:var(--link);margin:13px 0 6px;font-weight:700;white-space:nowrap}
.col .row{display:flex;gap:14px;font-size:12px;line-height:14px;color:#555;height:100px}
.col .thumb{width:130px;height:73px;flex:none}
.col ul{list-style:none;margin-top:8px}
.col li{font-size:12px;font-weight:700;color:var(--link);border-bottom:1px solid #e4e4e4;padding:3px 0 4px;height:22px;white-space:nowrap}
.ad{left:686px;top:176px;width:300px;height:250px;background:var(--ad);color:#fff;font-family:Arimo,sans-serif;font-weight:700;overflow:hidden}
.ad .big{position:absolute;left:18px;top:14px;font-size:40px;letter-spacing:-1px}
.ad .mid{position:absolute;left:20px;top:70px;font-size:22px;line-height:27px;font-weight:400}
.ad .date{position:absolute;left:20px;top:160px;font-size:15px}
.ad .band{position:absolute;left:0;top:212px;width:300px;height:38px;background:var(--ad-band);font-size:13px;padding:12px 20px}
.fb{left:691px;top:444px;width:293px;height:470px;border:1px solid #94a3c4;background:#fff;font-size:11px;color:#333;overflow:hidden}
.fb .hd{background:#eceff5;border-bottom:1px solid #ccc;padding:5px;font-weight:700;height:24px}
.post{display:flex;gap:8px;padding:8px 8px 0}
.av{width:40px;height:40px;flex:none;background:linear-gradient(#bbb,#777)}
.post b{color:#3b5998;display:block;margin-bottom:4px}
.post p{line-height:15px}
.post small{color:#888;display:block;margin-top:4px;font-size:10px}
.faces{display:flex;flex-wrap:wrap;gap:2px;width:270px;margin:8px 8px}
.faces span{width:42px;height:42px;background:linear-gradient(#a58e7c,#6a5a52)}
.foot{left:0;top:942px;width:1200px;height:209px;background:var(--foot);color:var(--foot-text);font-size:12.5px;letter-spacing:.3px}
.fcol{position:absolute;top:30px}
.fcol h4{font-family:"Roboto Condensed",sans-serif;font-weight:400;font-size:20px;color:#fff;margin-bottom:10px}
.fcol a{display:block;line-height:23px}
.fbrand{left:775px;top:56px;font-family:"Open Sans",sans-serif;font-size:32px;color:#e5e5e5;display:flex;gap:10px;align-items:center}
.fbrand i{width:26px;height:26px;border-radius:50%;background:#aaa;display:block}
.copy{left:765px;top:132px;width:315px;text-align:center;line-height:24px;font-size:13px}
</style>
</head>
<body>
<div class="page">
  <div class="abs brand"><i></i>Lumora Learning</div>
  <div class="abs search">Search<svg width="20" height="20" viewBox="0 0 20 20"><circle cx="8" cy="8" r="6" fill="none" stroke="#444" stroke-width="2"/><line x1="12" y1="12" x2="18" y2="18" stroke="#444" stroke-width="3"/></svg></div>
  <nav class="abs nav"><a class="on">Home</a><a>News</a><a>Comment</a><a>Features</a><a>Books</a><a>Ranking</a><a>Awards</a><a>Jobs</a><a>Subscribe</a><a style="border:0;box-shadow:none">Contact Us</a></nav>

  <div class="abs tag g" style="top:178px">Campus</div>
  <div class="abs tag b" style="top:219px">Springs</div>
  <div class="abs tag o" style="top:261px">Chinese</div>
  <div class="abs tag g" style="top:307px">Campus</div>
  <div class="abs tag b" style="top:349px">Springs</div>
  <div class="abs tag o" style="top:391px">Chinese</div>
  <div class="abs tag g" style="top:435px">Campus</div>
  <div class="abs tag b" style="top:478px">Springs</div>
  <div class="abs tag o" style="top:520px">Chinese</div>

  <div class="abs follow"><div style="padding-top:10px">Follow<br>Us</div><div class="rail"></div>
    <div class="soc">Pinboard</div><div class="soc">Worknet</div><div class="soc">Chirpline</div><div class="soc">Friendloop</div></div>

  <div class="abs photo" role="img" aria-label="Students writing at desks in a classroom" style="left:94px;top:177px;width:581px;height:291px;border:1px solid #ccc"></div>

  <section class="abs cat"><h2>Categories</h2>
    <div class="col" style="left:11px">
      <div class="pic photo" role="img" aria-label="Young pupils studying in class"></div>
      <h3>Halvorsen twins plan Coinvale trust</h3>
      <div class="row"><div class="thumb photo" role="img" aria-label="Two men in suits"></div><p>Tobin and Carver Halvorsen, famed for their legal dispute with Friendloop's Marek Zelinski, unveil plans to float a Coinvale trust.</p></div>
      <ul><li>Cathedral bank chief and deputy resign</li><li>Struggling Zentrix appoints Playcube boss</li><li>Portugal's finance minister quits</li><li>Firms' confidence 'at six-year high'</li></ul>
    </div>
    <div class="col" style="left:299px">
      <div class="pic photo" role="img" aria-label="Two smiling students at a computer"></div>
      <h3>Australia can select Farid for Summit Cup</h3>
      <div class="row"><div class="thumb photo" role="img" aria-label="Cricketer in training kit"></div><p>Pakistan-born off spinner Farid Amani can play for Australia in this summer's Summit Cup after receiving citizenship.</p></div>
      <ul><li>Sportsday - football transfers</li><li>Why 'Big Fred' should be cautious in victory</li><li>Fenwick: Rowley may want new challenge</li><li>Walden could make Australia comeback</li></ul>
    </div>
  </section>

  <aside class="abs ad"><div class="big">Be Prepared</div><div class="mid">Take part in a region-wide<br>safety drill for schools,<br>families and teachers.</div><div class="date">Regional Ready Week · October 2013</div><div class="band">www.readyweek.org</div></aside>

  <aside class="abs fb"><div class="hd">Find us on Friendloop</div>
    <div class="post" style="border-bottom:1px solid #ddd;padding-bottom:8px"><div class="av"></div><div><b>Dara Venn</b><p>✓ Like &nbsp;You like this.</p></div></div>
    <div class="post"><div class="av"></div><div><b>Dara Venn</b><p>I think all of Mexico should throw a party for my birthday this year. Does May 5th work for you?</p><small>18 hours ago</small></div></div>
    <div class="post"><div class="av"></div><div><b>Dara Venn</b><p>Chirpline wants to give you $50 in advertising credit for FREE. Such a deal! <span style="color:#3b5998">https://chirp.lnkimg.com/ DaraVenn</span></p><small>Thursday at 17:46 near Ridgefield, CO</small></div></div>
    <p style="margin:30px 8px 0;font-size:10px">You and 14,596 others like <span style="color:#3b5998">Dara Venn</span>.</p>
    <div class="faces" role="img" aria-label="Grid of fan profile pictures"><span></span><span></span><span></span><span></span><span></span><span></span><span></span><span></span><span></span><span></span><span></span><span></span></div>
    <p style="margin:10px 8px;font-size:9px;color:#666;border-top:1px solid #ddd;padding-top:4px">Friendloop social plugin</p>
  </aside>
</div>

<footer class="abs foot">
  <div class="fcol" style="left:131px"><h4>WHO WE ARE</h4><a>Company</a><a>News</a><a>Team</a><a>Careers</a><a>Contact</a></div>
  <div class="fcol" style="left:315px"><h4>WHAT WE DO</h4><a>What is Lumora Learning ?</a><a>Live Demo</a><a>Resources</a><a>FAQs</a><a>Mobile Apps</a></div>
  <div class="fcol" style="left:526px"><h4>WHO WE WORK WITH</h4><a>Utilities</a><a>Consumers</a><a>Partners</a><a>Get Started</a></div>
  <div class="abs fbrand"><i></i>Lumora Learning</div>
  <div class="abs copy">2006 - 2013 Lumora Learning Privacy Policy Terms of Conditions. All Rights Reserved</div>
</footer>
</body>
</html>
```